Redesign start page for existing online shop

We are selling building material (chimneys and flue pipes) as well as fireplaces (stoves). For this online shop we need a new start page. The domain is brunnfeld-bauwaren.de. Here you can see the current design. We want a smoother design with just one banner in the middle instead of the three in the first row. The look has to be more professional and trustworthy. You can therefore play with the colors. We want to try some different orange instead of our yellow / orange color. A few more things: - The phone number has to be bigger and more highlighted - So the 5 advantages at the top should be shown in a different way - New design for the products below - New footer

Target Market(s)

Germany and other countries in Europe.

Industry/Entity Type

Home Builder

Number of Pages Required

1 page

Other font styles liked:
• Please se the font on our current site.

Colors
f78f20
f68d4c

Requirements
Must have
• - Clear design - Trustworthy look - All elements Which are now shown shoulderstand be still there after redesigning -
Nice to have
• - See the Following sites to have a clou about our wishes: kalvesto.de flinkrabe.de

```html
<!DOCTYPE html>
<html lang="de">
<head>
<meta charset="utf-8">
<title>Brunnfeld Bauwaren – Schornsteine, Ofenrohre und Zubehör</title>
<link rel="stylesheet" href="https://fonts.googleapis.com/css2?family=Open+Sans:wght@400;600;700;800&display=swap">
<style>
:root{
  --orange:#f78f20;
  --orange-soft:#f68d4c;
  --orange-dark:#e07a12;
  --ink:#333333;
  --ink-soft:#555555;
  --muted:#888888;
  --line:#dddddd;
  --bar-dark:#3d3d3d;
  --bar-mid:#555555;
  --panel:#efefef;
  --cream:#faf3e8;
  --white:#ffffff;
}
*{box-sizing:border-box;margin:0;padding:0}
html,body{width:1200px;height:3082px;overflow:hidden}
body{font-family:"Open Sans",Arial,sans-serif;color:var(--ink);background:var(--white);font-size:12px;line-height:1.45}
.wrap{width:1080px;margin:0 auto;position:relative}
a{color:inherit;text-decoration:none}
.btn{display:inline-block;background:var(--orange);color:var(--white);font-weight:600;border-radius:3px}

/* top bar */
.topbar{height:35px;background:#f4f4f4;border-bottom:1px solid var(--line)}
.topbar .wrap{display:flex;align-items:center;justify-content:space-between;height:35px}
.topbar .quick{display:flex;gap:8px}
.topbar .quick a{background:var(--orange);color:#fff;font-size:9px;font-weight:700;padding:4px 12px;border-radius:2px;letter-spacing:.3px}
.topbar .account{display:flex;gap:22px;font-size:9px;font-weight:700;color:var(--ink-soft);align-items:center}
.stars{color:var(--orange);letter-spacing:1px;font-size:11px}

/* header */
.header{height:90px}
.header .wrap{display:flex;align-items:center;height:90px}
.brand{display:flex;align-items:center;gap:12px;width:400px}
.brand .mark{width:50px;height:50px;border-radius:50%;background:var(--orange)}
.brand .name{font-size:22px;font-weight:700;line-height:1.05;color:var(--ink-soft);letter-spacing:.5px}
.search{width:300px;height:34px;border:1px solid var(--line);border-radius:17px;position:relative;margin-left:60px}
.search svg{position:absolute;right:12px;top:8px}
.phone{margin-left:auto;text-align:left}
.phone .num{font-size:29px;font-weight:600;color:var(--orange);line-height:1.1;display:flex;align-items:center;gap:10px}
.phone .hours{font-size:11px;color:var(--ink-soft);margin-left:34px;letter-spacing:.3px}

/* navigation */
.nav{height:60px;border-bottom:1px solid var(--line)}
.nav .wrap{display:flex;align-items:center;height:60px}
.nav ul{list-style:none;display:flex;gap:48px;font-size:13px;font-weight:600;color:var(--ink)}
.rating{margin-left:auto;display:flex;align-items:center;gap:12px}
.rating .seal{width:52px;height:52px;border-radius:50%;background:#e9e9e9;border:3px solid #cfcfcf}
.rating .txt{font-size:10px;line-height:1.3;color:var(--ink-soft)}
.rating .txt b{font-size:13px;color:var(--ink)}

/* check bar */
.checkbar{height:30px;background:var(--bar-mid);color:#fff}
.checkbar .wrap{display:flex;gap:40px;align-items:center;height:30px;font-size:11px;font-weight:700;letter-spacing:.3px}
.checkbar span{display:flex;align-items:center;gap:6px}

/* hero */
.hero{height:397px;position:relative;overflow:hidden}
.hero .photo{position:absolute;inset:0;background:linear-gradient(100deg,#8c8478 0%,#b7b2aa 30%,#d6d3ce 55%,#c4c1bc 100%)}
.hero .copy{position:absolute;left:480px;top:100px;width:540px;text-align:center}
.hero h1{font-size:58px;font-weight:700;line-height:1.1;color:#fff;text-shadow:0 2px 6px rgba(0,0,0,.35)}
.hero .btn{margin-top:34px;padding:12px 30px;font-size:17px}
.recommend{position:absolute;left:855px;top:0;width:132px}
.recommend .label{background:var(--orange);color:#fff;font-size:9px;font-weight:700;text-align:center;padding:4px 0}
.recommend .seal{background:var(--orange-soft);height:104px;display:flex;align-items:center;justify-content:center}
.recommend .seal i{display:block;width:48px;height:56px;background:#2b2b2b}

/* advantages */
.advantages{height:50px;background:var(--bar-dark)}
.advantages .wrap{display:flex;justify-content:space-between;align-items:center;height:50px;font-size:14px;font-weight:700;color:var(--orange)}

/* brands */
.brands{height:103px;border-bottom:1px solid var(--line)}
.brands .wrap{display:flex;justify-content:space-around;align-items:center;height:103px}
.brands span{font-size:30px;font-weight:600}
.brands .b1{color:var(--orange)}
.brands .b2{color:#a33a1e;font-size:36px}
.brands .b3{color:var(--orange-dark);font-size:18px}
.brands .b4{color:var(--orange-soft);font-size:22px}

/* features */
.features{height:305px}
.features .wrap{display:grid;grid-template-columns:repeat(4,1fr);gap:40px;padding-top:45px}
.feature{text-align:center;padding:0 10px}
.feature svg{display:block;margin:0 auto 16px}
.feature h3{font-size:15px;font-weight:400;color:var(--ink-soft);line-height:1.35;margin-bottom:14px}
.feature p{font-size:10px;color:var(--ink-soft);line-height:1.55}

/* how it works */
.how{height:502px;padding-top:10px}
.how .box{width:1080px;height:492px;margin:0 auto;background:var(--panel);text-align:center;padding-top:40px}
.how h2{font-size:30px;font-weight:600;color:var(--ink)}
.how .lead{font-size:18px;color:var(--ink);margin-top:20px}
.steps{display:flex;justify-content:space-between;width:900px;margin:44px auto 0;position:relative}
.steps:before{content:"";position:absolute;left:60px;right:60px;top:56px;height:2px;background:#cfcfcf}
.step{width:180px;position:relative}
.step .ring{width:112px;height:112px;border-radius:50%;background:#fff;border:3px solid #cfcfcf;margin:0 auto;display:flex;align-items:center;justify-content:center}
.step p{font-size:13px;color:var(--ink);margin-top:16px;line-height:1.4}
.cta{display:flex;justify-content:center;align-items:center;gap:24px;margin-top:40px}
.cta strong{font-size:19px;font-weight:700}
.cta .btn{padding:9px 30px;font-size:14px}

/* products */
.products{height:568px;padding-top:53px}
.tabs{display:flex;gap:6px;height:35px}
.tabs span{border:1px solid var(--line);border-bottom:none;background:#f6f6f6;font-size:11px;padding:9px 20px 0;height:35px}
.tabs .active{background:#fff}
.panel{border:1px solid var(--line);height:480px;padding:30px 30px;display:flex;gap:30px}
.card{width:250px;text-align:center}
.card .img{height:330px;border:1px solid var(--line);position:relative;display:flex;justify-content:center;align-items:center}
.card .pipe{width:46px;height:280px;background:linear-gradient(90deg,#9a9a9a,#eeeeee 45%,#bcbcbc)}
.card .price{position:absolute;right:-1px;bottom:34px;background:var(--orange);color:#fff;font-size:16px;font-weight:700;padding:8px 14px}
.card h4{color:var(--orange);font-size:16px;font-weight:600;margin:16px 0 8px}
.card p{font-size:10px;color:var(--ink-soft);line-height:1.55;padding:0 10px}
.card .btn{margin-top:12px;padding:6px 20px;font-size:11px}
.desc{flex:1}
.desc h3{font-size:13px;font-weight:700;line-height:1.4;margin-bottom:14px;width:320px}
.desc .cols{display:grid;grid-template-columns:1fr 1fr;gap:34px;font-size:10px;line-height:1.6;color:var(--ink-soft)}
.desc .cols p{margin-bottom:14px}

/* seo */
.seo{height:655px;padding:10px 0}
.seo .inner{width:1200px;height:635px;background:var(--cream);padding:28px 60px 0}
.seo h2{color:var(--orange);font-size:18px;font-weight:600;text-align:center;margin-bottom:22px}
.seo .cols{display:grid;grid-template-columns:1fr 1fr;gap:50px;font-size:10px;line-height:1.6;color:var(--ink-soft)}
.seo p{margin-bottom:12px}
.seo h5{font-size:10px;font-weight:700;color:var(--ink);margin-bottom:8px}
.seo .hl{color:var(--orange)}

/* footer */
.foot{height:180px;background:#f0f0f0}
.foot .wrap{display:grid;grid-template-columns:360px 1fr 300px;gap:40px;padding-top:22px}
.promise{display:flex;gap:14px;margin-bottom:16px;font-size:9.5px;line-height:1.5;color:var(--ink-soft)}
.promise i{flex:0 0 56px;height:56px;display:block}
.promise .sq{background:#d7d7d7}
.promise .ci{border-radius:50%;background:#2f2f2f}
.foot h6{font-size:13px;font-weight:700;margin-bottom:12px}
.pay{display:grid;grid-template-columns:repeat(4,74px);gap:10px}
.pay span{height:34px;border:1px solid var(--line);background:#fff;display:flex;align-items:center;justify-content:center;font-size:10px;font-weight:700;color:var(--ink-soft)}
.contact ul{list-style:none;font-size:10.5px;line-height:1.65;color:var(--ink)}
.legal{height:107px;background:var(--bar-dark);color:#cfcfcf}
.legal .wrap{display:flex;justify-content:space-between;padding-top:22px;font-size:10.5px}
.legal .links p{line-height:2}
.legal .social{text-align:center}
.legal .social div{display:flex;gap:16px;font-size:11px;font-weight:600;color:#bbb}
.legal .social small{display:block;margin-top:16px;font-size:9px;color:#999}
.legal .info{text-align:right;line-height:1.7;font-size:9.5px;color:#aaa}
</style>
</head>
<body>

<div class="topbar">
  <div class="wrap">
    <div class="quick"><a href="#">SICHER EINKAUFEN ▾</a><a href="#">VORTEILE ▾</a><a href="#">BERATUNG &amp; KONTAKT ▾</a></div>
    <div class="account"><span><span class="stars">★★★★★</span> SEHR GUT (4.80/5.00)</span><span>MEIN KONTO</span><span>WARENKORB</span></div>
  </div>
</div>

<header class="header">
  <div class="wrap">
    <a class="brand" href="#"><span class="mark"></span><span class="name">BRUNNFELD<br>BAUWAREN</span></a>
    <div class="search">
      <svg width="16" height="16" viewBox="0 0 16 16"><circle cx="6.5" cy="6.5" r="5" fill="none" stroke="#f78f20" stroke-width="2"/><line x1="10.5" y1="10.5" x2="15" y2="15" stroke="#f78f20" stroke-width="2"/></svg>
    </div>
    <div class="phone">
      <div class="num"><svg width="22" height="22" viewBox="0 0 24 24"><path d="M6.6 10.8a15 15 0 0 0 6.6 6.6l2.2-2.2a1 1 0 0 1 1-.25 11 11 0 0 0 3.6.6 1 1 0 0 1 1 1V20a1 1 0 0 1-1 1A17 17 0 0 1 3 4a1 1 0 0 1 1-1h3.5a1 1 0 0 1 1 1 11 11 0 0 0 .6 3.6 1 1 0 0 1-.25 1z" fill="#f78f20"/></svg>08151 / 403 872 0</div>
      <div class="hours">MO. - FR. VON 09.00 BIS 18.00</div>
    </div>
  </div>
</header>

<nav class="nav">
  <div class="wrap">
    <ul><li>ONLINE SHOP ▾</li><li>SERVICE ▾</li><li>STANDORTE</li><li>FÜR HÄNDLER</li><li>INSTALLATEURE</li></ul>
    <div class="rating"><span class="seal"></span><div class="txt">Kundenbewertung<br><span class="stars">★★★★★</span><br>SEHR GUT<br><b>4.70</b> / 5.00</div></div>
  </div>
</nav>

<div class="checkbar">
  <div class="wrap">
    <span>✔ HEIZUNG INKL. MONTAGE</span><span>✔ FESTPREISANGEBOT</span><span>✔ KOSTENLOS &amp; UNVERBINDLICH</span>
  </div>
</div>

<section class="hero">
  <div class="photo" role="img" aria-label="Foto: Handwerker mit Rohrzange vor einem neu montierten Heizkessel an heller Wand"></div>
  <div class="wrap">
    <div class="copy">
      <h1>In 5 Minuten Zum Schornstein</h1>
      <a class="btn" href="#">Zum Angebot</a>
    </div>
    <div class="recommend"><div class="label">EMPFOHLEN VON</div><div class="seal"><i></i></div></div>
  </div>
</section>

<div class="advantages">
  <div class="wrap"><span>Deutsche Markenqualität</span><span>25 Jahre Garantie</span><span>Schnelle Lieferung</span><span>Kostenlose Fachberatung</span><span>Bundesweiter Montageservice</span></div>
</div>

<section class="brands">
  <div class="wrap"><span class="b1">Velstrand</span><span class="b2">Norvika</span><span class="b3">HESSLER OFEN</span><span class="b4">GLUTWERK</span></div>
</section>

<section class="features">
  <div class="wrap">
    <div class="feature">
      <svg width="60" height="64" viewBox="0 0 60 64"><rect x="12" y="4" width="36" height="48" fill="#e4e4e4" stroke="#aaa" stroke-width="2"/><line x1="19" y1="16" x2="41" y2="16" stroke="#aaa" stroke-width="2"/><line x1="19" y1="24" x2="41" y2="24" stroke="#aaa" stroke-width="2"/><line x1="19" y1="32" x2="34" y2="32" stroke="#aaa" stroke-width="2"/><circle cx="42" cy="50" r="10" fill="#f78f20"/><path d="M37 50l4 4 6-7" fill="none" stroke="#fff" stroke-width="2"/></svg>
      <h3>Verbindliches Heizungs Angebot sofort!</h3>
      <p>Geben Sie nur wenige Eckdaten zu Ihrem Haus in unseren Angebotsrechner ein und Sie erhalten innerhalb weniger Stunden ein verbindliches Angebot für Ihre neue Heizung!</p>
    </div>
    <div class="feature">
      <svg width="60" height="64" viewBox="0 0 60 64"><line x1="12" y1="12" x2="48" y2="52" stroke="#999" stroke-width="7" stroke-linecap="round"/><line x1="48" y1="12" x2="12" y2="52" stroke="#bbb" stroke-width="7" stroke-linecap="round"/></svg>
      <h3>Mehr als 30 Jahre Meisterqualität!</h3>
      <p>Erfahrung und Kompetenz sind der Garant für einen hervorragenden Service. Mit rund 100 geschulten und kompetenten Heizungsfachmännern sind wir deutschlandweit für Sie im Einsatz!</p>
    </div>
    <div class="feature">
      <svg width="60" height="64" viewBox="0 0 60 64"><rect x="10" y="6" width="40" height="50" fill="#e4e4e4" stroke="#aaa" stroke-width="2"/><polygon points="30,18 16,30 44,30" fill="#aaa"/><rect x="20" y="30" width="20" height="16" fill="#aaa"/></svg>
      <h3>Neue Heizung bereits ab 39 € im Monat!</h3>
      <p>Eine neue, umweltfreundliche und energiesparende Heizung liefern und installieren wir Ihnen bereits für 39,- Euro im Monat. Durch die mögliche Energieeinsparung ist Ihre Heizung fast geschenkt!</p>
    </div>
    <div class="feature">
      <svg width="60" height="64" viewBox="0 0 60 64"><circle cx="30" cy="32" r="24" fill="#e4e4e4" stroke="#aaa" stroke-width="2"/><path d="M30 16c6 8 10 12 10 20a10 10 0 0 1-20 0c0-6 4-10 10-20z" fill="#f78f20"/></svg>
      <h3>10 Jahre Garantie auf Ihre neue Heizung!</h3>
      <p>Wir vertrauen Qualität und bieten Ihnen daher ab sofort auf alle von uns eingebauten Heizkessel eine 10-Jahres-Garantie! So können Sie sich keine Sorgen mehr machen, falls Ihre Anlage doch einmal ausfallen sollte!</p>
    </div>
  </div>
</section>

<section class="how">
  <div class="box">
    <h2>So Funktioniert's</h2>
    <p class="lead">In wenigen Schritten zum richtigen Angebot für Ihre Sanierung</p>
    <div class="steps">
      <div class="step"><div class="ring"><svg width="50" height="50" viewBox="0 0 50 50"><rect x="8" y="10" width="34" height="24" rx="2" fill="none" stroke="#777" stroke-width="2.5"/><line x1="16" y1="42" x2="34" y2="42" stroke="#777" stroke-width="2.5"/><line x1="25" y1="34" x2="25" y2="42" stroke="#777" stroke-width="2.5"/></svg></div><p>Daten Online eingeben</p></div>
      <div class="step"><div class="ring"><svg width="50" height="50" viewBox="0 0 50 50"><polyline points="8,38 18,26 28,32 42,12" fill="none" stroke="#f78f20" stroke-width="3"/><line x1="6" y1="44" x2="44" y2="44" stroke="#777" stroke-width="2.5"/><line x1="6" y1="8" x2="6" y2="44" stroke="#777" stroke-width="2.5"/></svg></div><p>Aufmaß und Beratung<br>durch Kundenberater</p></div>
      <div class="step"><div class="ring"><svg width="50" height="50" viewBox="0 0 50 50"><rect x="12" y="6" width="26" height="34" fill="#fff" stroke="#777" stroke-width="2.5"/><rect x="18" y="12" width="26" height="34" fill="#fff" stroke="#777" stroke-width="2.5"/><line x1="23" y1="22" x2="39" y2="22" stroke="#777" stroke-width="2"/><line x1="23" y1="29" x2="39" y2="29" stroke="#777" stroke-width="2"/><line x1="23" y1="36" x2="33" y2="36" stroke="#777" stroke-width="2"/></svg></div><p>Angebot von 2 erfahrenen<br>Handwerkern</p></div>
      <div class="step"><div class="ring"><svg width="50" height="50" viewBox="0 0 50 50"><line x1="12" y1="38" x2="34" y2="16" stroke="#777" stroke-width="5" stroke-linecap="round"/><circle cx="36" cy="14" r="7" fill="none" stroke="#777" stroke-width="3"/></svg></div><p>Ausführung</p></div>
    </div>
    <div class="cta"><strong>Jetzt unverbindlich eine Anfrage stellen!</strong><a class="btn" href="#">Anfrage stellen ›</a></div>
  </div>
</section>

<section class="products">
  <div class="wrap">
    <div class="tabs"><span class="active">Preisbeispiel 1</span><span>Preisbeispiel 2</span><span>Preisbeispiel 3</span><span>Preisbeispiel 4</span><span>Preisbeispiel 5</span><span>Preisbeispiel 6</span><span>Preisbeispiel 7</span><span>Preisbeispiel 8</span></div>
    <div class="panel">
      <div class="card">
        <div class="img"><div class="pipe" role="img" aria-label="Produktfoto: Schornsteinverlängerung aus Edelstahl"></div><span class="price">ab € 63,00</span></div>
        <h4>Schornsteinverlängerung</h4>
        <p>Kaminverlängerungen frei konfigurierbar nach Ihren Wunschmaßen und in Handarbeit nach höchsten Ansprüchen hergestellt.</p>
        <a class="btn" href="#">Jetzt Ansehen ›</a>
      </div>
      <div class="desc">
        <h3>Schornsteinverlängerungen bzw. Kaminerhöhungen online bestellen</h3>
        <div class="cols">
          <div>
            <p>Eine Schornsteinverlängerung kann nötig werden, wenn der Schornstein einen zu geringen Zug aufweist oder die Höhe des Schornsteins nicht ausreichend ist. Dabei wird einfach die aus Edelstahl gefertigte Schornsteinverlängerung auf den gemauerten Schornstein aufgesetzt und mit Hilfe der Montageplatte befestigt. Die Schornsteinverlängerung gibt es in verschiedenen Ausführungen. Die einwandige Variante eignet sich als einfache Kaminerhöhung, um die Vorgaben des Schornsteinfegers nach einer bestimmten Höhe zu erfüllen. Die doppelwandige Ausführung wird dann genutzt, wenn das Entstehen von Kondensat eingeschränkt und die Verbrennung optimiert werden soll. Sie ist mit einer 32,5 mm dicken Wärmedämmung isoliert.</p>
            <p>Alle Kaminerhöhungen aus unserem Sortiment sind von hervorragender Qualität. Die Schornsteinverlängerungen werden in Deutschland aus hochwertigem Edelstahl gefertigt und erfüllen alle geltenden Zulassungsvoraussetzungen in Deutschland und vielen anderen Ländern der Europäischen Union. Deshalb erhalten Sie auch auf die von uns vertriebenen Schornsteinverlängerungen 25 Jahre Garantie auf</p>
          </div>
          <div>
            <p>Korrosionsbeständigkeit.</p>
            <p>Die einwandige Schornsteinverlängerung wie auch die doppelwandige Schornsteinverlängerung gibt es in Längen von 0,5 Meter bis zu 3 Meter. Die Durchmesser der Kaminerhöhung gehen von 115 mm bis 600 mm. Die Schornsteinverlängerungen bieten damit eine große Bandbreite von Anwendungsmöglichkeiten. Die Einbauhöhe der Verlängerung beträgt standardmäßig 250 mm, kann aber auch individuell bestellt werden. Auch die Abmessungen der Montageplatte sind frei wählbar, wobei das Standardmaß 400 mm x 400 mm beträgt.</p>
            <p>Eine Schornsteinverlängerung ist somit eine effektive Methode, den Schornstein zu verlängern. Die preiswerten Verlängerungen weisen eine hochwertige Verarbeitung auf und sind eine hervorragende Alternative zum Neubau des Schornsteins.</p>
          </div>
        </div>
      </div>
    </div>
  </div>
</section>

<section class="seo">
  <div class="inner">
    <h2>Edelstahlschornsteine, Schornsteinverlängerungen, Ofenrohre und Schornstein Zubehör – alles bei brunnfeld-bauwaren.de günstig kaufen.</h2>
    <div class="cols">
      <div>
        <p>Kann ich einen <span class="hl">Edelstahlschornstein</span> im Internet kaufen? Diese Frage haben Sie sich bestimmt auch schon gestellt. Bei anderen Waren ist der Online-Kauf längst selbstverständlich, doch bei Schornsteinen zögern viele noch. Dabei gibt es gute Gründe, die Anlage direkt beim Fachhändler im Netz zu bestellen: Sie sparen Zeit, vergleichen bequem und erhalten geprüfte Qualität zu fairen Preisen.</p>
        <p>Das Ziel war es, einen Onlineshop für Edelstahlschornsteine und Zubehör auf die Beine zu stellen, der nicht nur professionell, sondern auch nutzerfreundlich ist. Mit einer effizienten Organisation, modernen Fertigungsmethoden und langjähriger Erfahrung mit dem Produkt Edelstahlschornstein können wir diesen Anspruch erfüllen. Unser Team berät Sie kompetent bei allen Fragen rund um Ihr Vorhaben.</p>
        <h5>Edelstahlschornstein, Schornstein Bausatz und Edelstahlkamin – alles aus einer Hand.</h5>
        <p>Ob Sie einen doppelwandigen Edelstahlschornstein, eine Schornsteinsanierung für Ihren gemauerten Kamin oder einen Schornstein Bausatz suchen, hier werden Sie fündig. Bei Brunnfeld Bauwaren finden Sie eine große Auswahl an in Deutschland hergestellten Schornsteinen des Herstellers Talbrecht. Alle Produkte erfüllen die strengen Qualitätsvorschriften und sind dauerhaft bis zu 600 Grad temperaturbeständig.</p>
        <p>Und noch ein Tipp: Alle Schornsteine lassen sich wunderbar mit einem <span class="hl">Ofenrohr</span> von Talbrecht kombinieren. Hier gibt es eine große Auswahl an verschiedenen Längen, Farben und Winkeln. Außerdem sind seit kurzem auch isolierte Ofenrohre lieferbar, mit denen sich der Abstand zu brennbaren Materialien verringern lässt.</p>
        <h5>Schornsteinverlängerung und Kaminverlängerungen günstig selbst aufbauen.</h5>
        <p>Aufgrund neuerer Verordnungen reicht oft die Höhe eines bestehenden Schornsteins nicht mehr aus. Durch bauliche Veränderungen der Umgebung oder aus anderen Gründen kann es dazu kommen, dass eine Verlängerung nötig wird. In unserem Shop finden Sie <span class="hl">Kaminverlängerungen</span> in vielen Ausführungen, die nach Maß gefertigt werden und sich leicht montieren lassen.</p>
      </div>
      <div>
        <h5>Leichtbauschornstein F90 und eine Wanddurchführung: Brandschutz auf höchstem Niveau.</h5>
        <p>Ein Edelstahlschornstein eignet sich hervorragend als nachträgliche Abgasleitung neben einem bereits gemauerten Schornstein im Gebäude. Was aber, wenn Ihnen die Optik nicht zusagt oder der Platz fehlt? Dafür ist der <span class="hl">Leichtbauschornstein</span> die ideale Lösung. In Verbindung mit einer feuerfesten <span class="hl">Wanddurchführung</span> haben Sie hier das perfekte Duo für einen sicheren Zusatzschornstein.</p>
        <h5>Schornsteinabdeckung, Kaminabdeckung und Kaminabdeckplatte aus Edelstahl nach Maß.</h5>
        <p>Ältere Schornsteinköpfe unterliegen starken Belastungen durch Witterungseinflüsse. Nach vielen Jahren des Regens, Sonnenscheins, der Kälte und der Wärme werden Schornsteinköpfe porös und beginnen zu bröckeln. Dann wird es höchste Zeit für eine Kaminabdeckplatte oder eine <span class="hl">Schornsteinabdeckung</span>. Bei Kaminabdeckungen gibt es die bekannte Kapuzenvariante und weitere Formen, die alle individuell nach Maß gefertigt werden.</p>
        <h5>Rauchsauger, Zugbegrenzer, Kaminfüsse und andere Spezialprodukte</h5>
        <p>Im Sortiment dieses Onlineshops finden Sie auch noch viele weitere Produkte rund um das Thema Schornstein und Abgastechnik. Hier wäre beispielsweise der <span class="hl">Rauchsauger</span> zu nennen. Ein sehr wichtiges Gerät, mit dem Sie den Schornsteinzug elektrisch verstärken können. Ebenfalls aus der Kategorie der Zugregelung und Zugverbesserung gibt es den Zugbegrenzer, der den Zug mechanisch reguliert.</p>
        <p>Viel Spaß beim Einkaufen, wünscht Ihnen das Team von brunnfeld-bauwaren.de!</p>
      </div>
    </div>
  </div>
</section>

<footer>
  <div class="foot">
    <div class="wrap">
      <div>
        <div class="promise"><i class="sq"></i><p>Wir beziehen ausschließlich Waren von deutschen Markenherstellern. Unser gesamtes Sortiment wird von Fachbetrieben in Deutschland gefertigt und geprüft. Für Ihre Sicherheit nur das Beste zum fairen Preis.</p></div>
        <div class="promise"><i class="ci"></i><p>Um unsere Preisansprüche und unseren Leistungsanspruch gerecht zu werden, bieten wir Ihnen 25 Jahre Garantie auf alle Edelstahlschornsteine und Bauteile.</p></div>
      </div>
      <div>
        <h6>Zahlungsarten</h6>
        <div class="pay"><span>Amvera</span><span>Vistra</span><span>Mondcard</span><span>Direktpay</span><span>Paywell</span><span>Vorkasse</span><span>Lastschrift</span></div>
      </div>
      <div class="contact">
        <h6>Kostenlose Beratung</h6>
        <ul><li>• 08151 / 403 872 0</li><li>• Mo. - Fr. von 09:00 bis 18:00</li><li>• info@brunnfeld-bauwaren.de</li><li>• Ahornstraße 7</li><li>&nbsp;&nbsp;80331 München</li><li>&nbsp;&nbsp;Deutschland</li></ul>
      </div>
    </div>
  </div>
  <div class="legal">
    <div class="wrap">
      <div class="links"><p>Häufige Fragen | AGB | Lieferung &amp; Zahlung | Impressum | Blog</p><p>Über uns | Widerruf | Datenschutz | Kontaktieren Sie uns | Glossar</p></div>
      <div class="social"><div><span>Kvell</span><span>Strom</span><span>Ortl</span><span>Vidra</span><span>Pinna</span></div><small>© 2011 - 2016 Brunnfeld GmbH</small></div>
      <div class="info">Brunnfeld Bauwaren<br>Durchschnittliche Bewertung: 4.71 (von 5)<br>Ermittelt aus 285 Bewertungen.</div>
    </div>
  </div>
</footer>

</body>
</html>
```